Need updated stationery design for chiropractic clinic

We recently moved our office and are looking to refresh our letterhead, business cards, presentation folder and envelopes. I tend to prefer simple, clean designs. We communicate with a lot of attorneys and want to exude professionalism. I have attached our logo and 2 additional versions (all white and white letters instead of grey).

Target Market(s)

Other medical professionals and attorneys. Business cards will go to patients as well.

Industry/Entity Type

Healthcare

```html
<!DOCTYPE html>
<html lang="en">
<head>
<meta charset="UTF-8">
<title>Harborline Care – Envelope</title>
<link rel="stylesheet" href="https://fonts.googleapis.com/css2?family=Montserrat:wght@400;500&family=Roboto:wght@700&display=swap">
<style>
  :root {
    --brand-blue: #1b9bd0;
    --brand-teal: #3bbfcc;
    --soft-teal: #a8dde0;
    --soft-blue: #98c3e4;
    --ink-grey: #555555;
    --edge: #444444;
    --paper: #ffffff;
  }
  * { margin: 0; padding: 0; box-sizing: border-box; }
  html, body { width: 1200px; height: 1000px; overflow: hidden; background: var(--paper); }
  .canvas { position: relative; width: 1200px; height: 1000px; font-family: "Montserrat", sans-serif; }

  /* Front of envelope */
  .envelope-front {
    position: absolute; left: 74px; top: 30px; width: 1052px; height: 457px;
    border: 1px solid var(--edge); border-bottom: none; overflow: hidden; background: var(--paper);
  }
  .brand {
    position: absolute; left: 83px; top: 72px; display: flex; align-items: center; gap: 12px;
  }
  .brand-square { width: 30px; height: 30px; background: var(--brand-blue); }
  .brand-name {
    font-family: "Roboto", sans-serif; font-weight: 700; font-size: 30px; color: var(--brand-blue);
    letter-spacing: -0.3px;
  }
  .corner-art {
    position: absolute; left: 652px; top: 42px; width: 373px; height: 282px;
    background: linear-gradient(135deg, var(--soft-teal) 0%, var(--soft-blue) 100%);
    opacity: 0.55;
  }
  .contact-band {
    position: absolute; left: 0; top: 324px; width: 100%; height: 133px; background: var(--brand-blue);
  }
  .contact-item {
    position: absolute; display: flex; align-items: center; gap: 16px;
    color: var(--paper); font-size: 14px; font-weight: 400; line-height: 1; white-space: nowrap;
  }
  .contact-item svg { width: 17px; height: 17px; flex: none; }
  .contact-phone { left: 82px; top: 42px; }
  .contact-email { left: 82px; top: 73px; }
  .contact-web { left: 286px; top: 42px; }
  .contact-address { left: 286px; top: 73px; }

  /* Back of envelope */
  .envelope-back { position: absolute; left: 0; top: 0; width: 1200px; height: 1000px; }
  .flap-name {
    position: absolute; left: 0; top: 558px; width: 1200px; text-align: center;
    font-family: "Roboto", sans-serif; font-weight: 700; font-size: 28px; color: var(--paper);
  }
</style>
</head>
<body>
<div class="canvas">

  <section class="envelope-front">
    <div class="brand">
      <span class="brand-square"></span>
      <span class="brand-name">Harborline Care</span>
    </div>

    <div class="corner-art" role="img" aria-label="Large soft decorative brand motif in pale teal and blue"></div>

    <div class="contact-band">
      <div class="contact-item contact-phone">
        <svg viewBox="0 0 24 24" fill="none" stroke="#fff" stroke-width="1.6" stroke-linejoin="round"><path d="M5 3h4l2 5-2.5 1.5a11 11 0 0 0 6 6L16 13l5 2v4a2 2 0 0 1-2 2A16 16 0 0 1 3 5a2 2 0 0 1 2-2z"/></svg>
        <span>+000-555-0142</span>
      </div>
      <div class="contact-item contact-email">
        <svg viewBox="0 0 24 24" fill="none" stroke="#fff" stroke-width="1.6"><rect x="3" y="6" width="18" height="12"/><path d="M3 6l9 7 9-7"/></svg>
        <span>care@harborline.uk</span>
      </div>
      <div class="contact-item contact-web">
        <svg viewBox="0 0 24 24" fill="none" stroke="#fff" stroke-width="1.6"><circle cx="12" cy="12" r="9"/><path d="M3 12h18M12 3c3 3 3 15 0 18M12 3c-3 3-3 15 0 18"/></svg>
        <span>harborline.uk</span>
      </div>
      <div class="contact-item contact-address">
        <svg viewBox="0 0 24 24" fill="none" stroke="#fff" stroke-width="1.6"><path d="M12 21s-6-6.5-6-11a6 6 0 0 1 12 0c0 4.5-6 11-6 11z"/><circle cx="12" cy="10" r="2.2"/></svg>
        <span>48 Quay Lane, Eastbridge, UK</span>
      </div>
    </div>
  </section>

  <svg class="envelope-back" viewBox="0 0 1200 1000" aria-hidden="true">
    <rect x="74.5" y="513.5" width="1051" height="455" fill="#fff" stroke="var(--edge)" stroke-width="1"/>
    <path d="M87 615 L75 968 M1113 615 L1125 968" stroke="#bbbbbb" stroke-width="1" fill="none"/>
    <path d="M75 513 L1125 513 L1112 605 Q1108 635 1080 635 L118 635 Q91 635 87 605 Z" fill="var(--brand-blue)"/>
  </svg>
  <div class="flap-name">Harborline Care</div>

</div>
</body>
</html>
```